new roofing company card

New primary business card for roofing company.

Industry/Entity Type

Residential roofing/Specializing in Asphalt and Standing seam metal roofing

Contact Information for Business Card

Phone number is: 484 672 1058 Email: support@fennridgeroofworks.com website: www.fennridgeroofworks.com

Colors
EB3D1F
EC4F4E
F09395
F8D3D4
FCEDEE

```html
<!DOCTYPE html>
<html lang="en">
<head>
<meta charset="UTF-8">
<title>Fennridge Roofworks – Business Card</title>
<link href="https://fonts.googleapis.com/css2?family=Libre+Baskerville:wght@400;700&family=Arimo:wght@400&display=swap" rel="stylesheet">
<style>
  :root {
    --stage: #3b3c40;
    --paper: #f7f7f5;
    --ink: #1f201f;
    --card-dark: #1c1d1c;
    --brand-red: #c9271f;
    --text-grey: #4a4a4a;
    --rule-grey: #8a8a8a;
    --white: #ffffff;
  }
  * { box-sizing: border-box; margin: 0; padding: 0; }
  html, body {
    width: 1200px; height: 900px; overflow: hidden;
    background: var(--stage);
  }
  .stage {
    position: relative; width: 1200px; height: 900px;
    display: flex; flex-direction: column; align-items: center; justify-content: center; gap: 46px;
  }
  .card {
    width: 660px; height: 377px; position: relative;
    box-shadow: 0 10px 24px rgba(0,0,0,0.35);
  }
  .card-front {
    background: var(--paper);
    display: flex; align-items: center;
  }
  .front-brand {
    width: 300px; padding-left: 40px;
    display: flex; align-items: center; gap: 12px;
  }
  .brand-mark {
    width: 18px; height: 18px; background: var(--brand-red); flex: none;
  }
  .brand-name {
    font-family: "Libre Baskerville", serif; font-weight: 700;
    color: var(--ink); font-size: 24px; line-height: 1.15; letter-spacing: 1px;
    text-transform: uppercase;
  }
  .divider {
    width: 1px; height: 150px; background: var(--rule-grey);
  }
  .front-details { padding-left: 32px; }
  .person-name {
    font-family: "Libre Baskerville", serif; font-weight: 700;
    color: var(--brand-red); font-size: 22px; text-transform: uppercase; letter-spacing: 0.5px;
  }
  .person-role {
    font-family: "Arimo", sans-serif; color: var(--text-grey); font-size: 16px;
    margin-top: 4px; margin-bottom: 20px;
  }
  .contact-list { list-style: none; }
  .contact-item {
    display: flex; align-items: center; gap: 9px;
    font-family: "Arimo", sans-serif; color: var(--text-grey); font-size: 16px;
    margin-bottom: 6px;
  }
  .contact-icon { width: 15px; height: 15px; flex: none; }
  .card-back {
    background: var(--card-dark);
    display: flex; align-items: center; justify-content: center; gap: 18px;
  }
  .card-back .brand-mark { width: 26px; height: 26px; }
  .card-back .brand-name {
    color: var(--white); font-size: 40px; text-align: left;
  }
</style>
</head>
<body>
<main class="stage">
  <section class="card card-front">
    <div class="front-brand">
      <span class="brand-mark"></span>
      <p class="brand-name">Fennridge<br>Roofworks</p>
    </div>
    <div class="divider"></div>
    <div class="front-details">
      <h1 class="person-name">Daniel Harlow</h1>
      <p class="person-role">Manager</p>
      <ul class="contact-list">
        <li class="contact-item">
          <svg class="contact-icon" viewBox="0 0 16 16" aria-hidden="true"><path fill="#c9271f" d="M2 5c0-2 2-3 6-3s6 1 6 3v1h-3V5H5v1H2z M4 7h8l2 6H2z"/><circle cx="8" cy="10" r="1.6" fill="#f7f7f5"/></svg>
          <span>484 672 1058</span>
        </li>
        <li class="contact-item">
          <svg class="contact-icon" viewBox="0 0 16 16" aria-hidden="true"><rect x="1" y="3" width="14" height="10" fill="#c9271f"/><path d="M1.5 3.5 8 9l6.5-5.5" fill="none" stroke="#f7f7f5" stroke-width="1.3"/></svg>
          <span>support@fennridgeroofworks.com</span>
        </li>
        <li class="contact-item">
          <svg class="contact-icon" viewBox="0 0 16 16" aria-hidden="true"><circle cx="8" cy="8" r="7" fill="#c9271f"/><path d="M1 8h14M8 1c-3 3-3 11 0 14M8 1c3 3 3 11 0 14" fill="none" stroke="#f7f7f5" stroke-width="1"/></svg>
          <span>www.fennridgeroofworks.com</span>
        </li>
      </ul>
    </div>
  </section>
  <section class="card card-back">
    <span class="brand-mark"></span>
    <p class="brand-name">Fennridge<br>Roofworks</p>
  </section>
</main>
</body>
</html>
```